Drywall plastering business card design

Attached is my new logo and a picture of my current business card. I would like my new logo incorporated in to the business card and also my website which is:
www.ridgecrestwallfinishers.co.nz
Industry/Entity Type
Business
Contact Information for Business Card
I would like a picture of my van and my new logo on my new business card. See attached files for pictures of my old business card, van picture and logo.
Colors
0555a3
ffffff
Requirements
Must have
- New logo, Van, contact info

```html
<!DOCTYPE html>
<html lang="en">
<head>
<meta charset="utf-8">
<title>Ridgecrest Wall Finishers – Business Card</title>
<link href="https://fonts.googleapis.com/css2?family=Open+Sans:wght@400;600;700;800&family=Roboto+Condensed:wght@400&display=swap" rel="stylesheet">
<style>
  :root {
    --backdrop: #e9eaec;
    --card: #ffffff;
    --brand-blue: #1e88d8;
    --ink: #2b2b2b;
    --muted: #555a60;
    --divider: #eceef0;
  }
  * { box-sizing: border-box; margin: 0; padding: 0; }
  html, body { width: 1200px; height: 852px; overflow: hidden; }
  body {
    background: var(--backdrop);
    font-family: "Open Sans", sans-serif;
    position: relative;
  }
  .card {
    position: absolute;
    width: 540px;
    height: 310px;
    background: var(--card);
    border-radius: 12px;
    overflow: hidden;
    box-shadow: 0 6px 18px rgba(0,0,0,0.12);
  }
  .card--front { left: 40px; top: 271px; }
  .card--back { left: 620px; top: 271px; }

  .brand {
    position: absolute;
    display: flex;
    align-items: center;
    gap: 14px;
  }
  .brand__mark {
    width: 22px; height: 22px;
    border-radius: 50%;
    background: var(--brand-blue);
    flex: none;
  }
  .brand__name {
    font-weight: 800;
    color: var(--brand-blue);
    text-transform: uppercase;
    line-height: 1.05;
  }
  .card--front .brand { left: 50%; top: 50%; transform: translate(-50%, -50%); }
  .card--front .brand__name { font-size: 34px; }

  .card--back .brand { left: 30px; top: 50%; transform: translateY(-50%); }
  .card--back .brand__name { font-size: 22px; }

  .details {
    position: absolute;
    left: 270px; top: 0; right: 0; bottom: 10px;
    border-left: 1px solid var(--divider);
    padding: 48px 20px 0 22px;
  }
  .details__name {
    font-weight: 700;
    font-size: 17px;
    letter-spacing: 0.5px;
    color: var(--brand-blue);
  }
  .details__role { font-size: 12px; color: var(--muted); margin: 2px 0 0 14px; }
  .contact { list-style: none; margin-top: 34px; }
  .contact li {
    display: flex; align-items: center; gap: 10px;
    font-family: "Roboto Condensed", sans-serif;
    font-size: 12.5px; color: var(--ink);
    margin-bottom: 7px;
    white-space: nowrap;
  }
  .contact svg { width: 12px; height: 12px; flex: none; fill: var(--brand-blue); }
  .tagline {
    margin-top: 8px; margin-left: 22px;
    font-size: 14px; color: var(--brand-blue);
    text-transform: uppercase; line-height: 1.35;
  }
  .card__band {
    position: absolute; left: 0; right: 0; bottom: 0; height: 10px;
    background: var(--brand-blue);
  }
</style>
</head>
<body>
  <section class="card card--front" aria-label="Business card front">
    <div class="brand">
      <span class="brand__mark"></span>
      <span class="brand__name">Ridgecrest<br>Wall Finishers</span>
    </div>
  </section>

  <section class="card card--back" aria-label="Business card back">
    <div class="brand">
      <span class="brand__mark"></span>
      <span class="brand__name">Ridgecrest<br>Wall Finishers</span>
    </div>
    <div class="details">
      <p class="details__name">DAN MARSH</p>
      <p class="details__role">Proprietor</p>
      <ul class="contact">
        <li>
          <svg viewBox="0 0 24 24" aria-hidden="true"><path d="M6.6 10.8a15 15 0 0 0 6.6 6.6l2.2-2.2a1 1 0 0 1 1-.25 11.4 11.4 0 0 0 3.6.57 1 1 0 0 1 1 1V20a1 1 0 0 1-1 1A17 17 0 0 1 3 4a1 1 0 0 1 1-1h3.5a1 1 0 0 1 1 1c0 1.25.2 2.45.57 3.6a1 1 0 0 1-.25 1z"/></svg>
          027 555 01 42
        </li>
        <li>
          <svg viewBox="0 0 24 24" aria-hidden="true"><path d="M2 5h20v14H2z M2 5l10 8 10-8" fill="none" stroke="currentColor" style="stroke:var(--brand-blue)" stroke-width="2.2"/></svg>
          ridgecrestwallfinishers@mail.co.nz
        </li>
        <li>
          <svg viewBox="0 0 24 24" aria-hidden="true"><circle cx="12" cy="12" r="10"/><path d="M2 12h20M12 2c3 3 3 17 0 20M12 2c-3 3-3 17 0 20" fill="none" stroke="#fff" stroke-width="1.4"/></svg>
          www.ridgecrestwallfinishers.co.nz
        </li>
      </ul>
      <p class="tagline">Large jobs or small -<br>always quality assured</p>
    </div>
    <div class="card__band"></div>
  </section>
</body>
</html>
```